Business card for Chiropractic clinics needs reworked / redesigned

The business card in attachment was designed 10 years ago. It is in need of an update.
We have 2 clinics:
VELDHOVE KLINIEK & VELDHOVE KLINIEK NOORD
Only one address needs to be on the card for doctors that only work in one clinic and two addresses need to be on the card for the doctors that work in both clinics.

Target Market(s)

patients/referrers

Industry/Entity Type

Medical

Contact Information for Business Card

Logo (in full or zoomed-in)
Clinic Name
Doctor name and title
clinic address, website, tel, email

Font styles to use
Sans Serif

Colors

Designer to choose colors to be used in the design.

Requirements
Must have
• Good contrast/readability
• We like modern minimalistic designs
• The Bcard needs to project our very high standard of proficiency/professionalism
Should not have
• Not curly
• Not to much colours

```html
<!DOCTYPE html>
<html lang="nl">
<head>
<meta charset="utf-8">
<title>Veldhove Kliniek – visitekaartje</title>
<link rel="stylesheet" href="https://fonts.googleapis.com/css2?family=Roboto+Condensed:wght@700&family=Roboto:wght@300;400&display=swap">
<style>
  :root {
    --backdrop: #ece8e1;
    --card: #243a3c;
    --card-shadow: rgba(0, 0, 0, 0.28);
    --mark-light: #5f8384;
    --mark-dark: #2b4547;
    --text-strong: #ffffff;
    --text-soft: #e3e9e9;
    --rule: #ffffff;
  }
  * { box-sizing: border-box; margin: 0; padding: 0; }
  html, body {
    width: 1200px;
    height: 800px;
    overflow: hidden;
    background: var(--backdrop);
  }
  .canvas {
    position: relative;
    width: 1200px;
    height: 800px;
  }
  .card {
    position: absolute;
    top: 271px;
    width: 450px;
    height: 257px;
    background: var(--card);
    box-shadow: 0 6px 14px var(--card-shadow);
    overflow: hidden;
    color: var(--text-strong);
  }
  .card--front { left: 132px; }
  .card--back  { left: 619px; }

  .card__mark-area {
    position: absolute;
    left: 43px;
    top: 0;
    width: 100px;
    height: 257px;
  }

  .front-title {
    position: absolute;
    left: 134px;
    top: 38px;
    font-family: "Roboto Condensed", "Arial Narrow", sans-serif;
    font-weight: 700;
    font-size: 24px;
    line-height: 31px;
  }
  .front-title__name { display: block; }
  .front-title__sub  { display: block; font-size: 22px; }

  .contact {
    position: absolute;
    right: 33px;
    text-align: right;
    font-family: "Roboto", Arial, sans-serif;
  }
  .doctor { top: 20px; }
  .doctor__name {
    font-family: "Roboto Condensed", "Arial Narrow", sans-serif;
    font-weight: 700;
    font-size: 17px;
    line-height: 20px;
  }
  .doctor__title {
    font-weight: 300;
    font-size: 11px;
    letter-spacing: 0.3px;
    color: var(--text-soft);
  }
  .clinic { line-height: 18.5px; }
  .clinic--main  { top: 78px; }
  .clinic--north { top: 170px; }
  .clinic__name {
    font-family: "Roboto Condensed", "Arial Narrow", sans-serif;
    font-weight: 700;
    font-size: 13.5px;
  }
  .clinic__line {
    font-weight: 300;
    font-size: 13px;
    color: var(--text-soft);
  }
  .clinic-divider {
    position: absolute;
    left: 216px;
    top: 160px;
    width: 201px;
    height: 1.5px;
    background: var(--rule);
  }
</style>
</head>
<body>
<main class="canvas">

  <section class="card card--front" aria-label="Voorkant visitekaartje">
    <svg class="card__mark-area" role="img" aria-label="Plaats voor het kliniekmerk: gestileerde rug en wervelkolom" viewBox="0 0 100 257" preserveAspectRatio="none">
      <defs>
        <linearGradient id="mark-fade-front" x1="0" y1="0" x2="1" y2="0">
          <stop offset="0" stop-color="var(--mark-dark)"/>
          <stop offset="0.5" stop-color="var(--mark-light)" stop-opacity="0.35"/>
          <stop offset="1" stop-color="var(--mark-dark)"/>
        </linearGradient>
      </defs>
      <rect width="100" height="257" fill="url(#mark-fade-front)"/>
    </svg>
    <h1 class="front-title">
      <span class="front-title__name">VELDHOVE</span>
      <span class="front-title__sub">kliniek</span>
      <span class="front-title__sub">kliniek noord</span>
    </h1>
  </section>

  <section class="card card--back" aria-label="Achterkant visitekaartje">
    <svg class="card__mark-area" role="img" aria-label="Plaats voor het kliniekmerk: gestileerde rug en wervelkolom" viewBox="0 0 100 257" preserveAspectRatio="none">
      <defs>
        <linearGradient id="mark-fade-back" x1="0" y1="0" x2="1" y2="0">
          <stop offset="0" stop-color="var(--mark-dark)"/>
          <stop offset="0.5" stop-color="var(--mark-light)" stop-opacity="0.35"/>
          <stop offset="1" stop-color="var(--mark-dark)"/>
        </linearGradient>
      </defs>
      <rect width="100" height="257" fill="url(#mark-fade-back)"/>
    </svg>

    <div class="contact doctor">
      <p class="doctor__name">Laurent VERBEKE D.C.</p>
      <p class="doctor__title">CHIROPRACTOR</p>
    </div>

    <address class="contact clinic clinic--main" style="font-style:normal">
      <p class="clinic__name">VELDHOVE KLINIEK</p>
      <p class="clinic__line">Lindelaan 148</p>
      <p class="clinic__line">09 555 01 42</p>
      <p class="clinic__line">veldhovekliniek.be</p>
    </address>

    <div class="clinic-divider"></div>

    <address class="contact clinic clinic--north" style="font-style:normal">
      <p class="clinic__name">VELDHOVE KLINIEK NOORD</p>
      <p class="clinic__line">Kerkstraat 27</p>
      <p class="clinic__line">09 555 08 19</p>
      <p class="clinic__line">veldhovekliniek.be</p>
    </address>
  </section>

</main>
</body>
</html>
```